Billboard

we want our Hop & Skip logo really big, we need this to stand out

Use a really bold font for the wording as it's on a billboard on the highway

Hop & Skip Logo
perhaps on left hand side really large then have a slanting line and a different colour background for the other side.

Wording BELOW-bold

TOUR NOW

hopandskip.edu.au

Use one image,
I have attached other designs we have been using for our campaign so a similar look would be great.
specs- 1224 W × 324 H px JPEG

Target Market(s)
families

Industry/Entity Type
childcare

Target Market(s)

families

Industry/Entity Type

childcare

Requirements
Must have
• bold font and big logo

```html
<!DOCTYPE html>
<html lang="en">
<head>
<meta charset="utf-8">
<title>Hop &amp; Skip – Tour Now Billboard</title>
<link rel="stylesheet" href="https://fonts.googleapis.com/css2?family=Poppins:wght@400;800&display=swap">
<style>
  :root {
    --sky-blue: #00aeef;
    --sun-yellow: #fbff00;
    --white: #ffffff;
    --ink: #111111;
    --stage: #333333;
    --photo-warm: #c98a4e;
    --photo-deep: #5a3a22;
    --photo-light: #e9b679;
  }
  html, body {
    margin: 0;
    width: 1200px;
    height: 1200px;
    overflow: hidden;
    background: var(--stage);
  }
  .stage {
    width: 1200px;
    height: 1200px;
    display: flex;
    align-items: center;
    justify-content: center;
  }
  .billboard {
    width: 1100px;
    height: 291px;
    display: block;
    box-shadow: 0 12px 30px rgba(0,0,0,0.45);
  }
  .headline {
    font-family: "Poppins", sans-serif;
    font-weight: 800;
    fill: var(--white);
  }
  .web-address {
    font-family: "Poppins", sans-serif;
    font-weight: 400;
    fill: var(--ink);
  }
  .brand-name {
    font-family: "Poppins", sans-serif;
    font-weight: 800;
    fill: var(--white);
  }
</style>
</head>
<body>
<main class="stage">
  <svg class="billboard" viewBox="0 0 1692 448" xmlns="http://www.w3.org/2000/svg">
    <defs>
      <linearGradient id="photoTone" x1="0" y1="0" x2="0.6" y2="1">
        <stop offset="0" stop-color="var(--photo-deep)"/>
        <stop offset="0.45" stop-color="var(--photo-warm)"/>
        <stop offset="1" stop-color="var(--photo-light)"/>
      </linearGradient>
    </defs>

    <!-- main background -->
    <rect class="panel-blue" x="0" y="0" width="1692" height="448" fill="var(--sky-blue)"/>

    <!-- photo area -->
    <polygon class="photo-area" role="img"
      aria-label="Photo of smiling toddlers in sun hats playing with buckets and spades in a sandpit"
      points="0,0 612,0 840,224 612,448 0,448" fill="url(#photoTone)"/>

    <!-- white chevron stripe -->
    <path class="chevron-stripe" d="M612,0 L660,0 L880,210 Q893,224 880,238 L660,448 L612,448 L840,224 Z" fill="var(--white)"/>

    <!-- yellow wedges -->
    <path class="wedge-top" d="M660,0 L845,0 Q866,8 858,30 L790,128 Z" fill="var(--sun-yellow)"/>
    <path class="wedge-bottom" d="M660,448 L845,448 Q866,440 858,418 L790,320 Z" fill="var(--sun-yellow)"/>

    <!-- logo block -->
    <path class="logo-block" d="M0,0 L190,0 L245,58 Q256,70 245,82 L95,230 Q80,244 66,230 L0,160 Z" fill="var(--sky-blue)"/>
    <circle class="logo-dot" cx="95" cy="52" r="24" fill="var(--sun-yellow)"/>
    <text class="brand-name" x="95" y="120" font-size="40" text-anchor="middle">Hop &amp;</text>
    <text class="brand-name" x="95" y="162" font-size="40" text-anchor="middle">Skip</text>

    <!-- headline -->
    <text class="headline" x="1266" y="244" font-size="124" text-anchor="middle">TOUR NOW</text>

    <!-- web address band -->
    <path class="url-band" d="M950,448 L1030,372 Q1042,362 1058,362 L1692,362 L1692,448 Z" fill="var(--sun-yellow)"/>
    <g class="globe-icon" transform="translate(1098,405)" fill="none" stroke="var(--ink)">
      <circle r="21" fill="var(--ink)"/>
      <circle r="13" stroke="var(--white)" stroke-width="2.5"/>
      <ellipse rx="5.5" ry="13" stroke="var(--white)" stroke-width="2.5"/>
      <line x1="-13" y1="0" x2="13" y2="0" stroke="var(--white)" stroke-width="2.5"/>
    </g>
    <text class="web-address" x="1140" y="422" font-size="50">hopandskip.edu.au</text>
  </svg>
</main>
</body>
</html>
```